Create a banner for me that embodies my health and well being package.

I am an intuitive counselor with a busy practice helping clients to shift their blocks and move forward in their lives.
I have created a package called '9 paths home again'
I am wanting a banner to put on my website page, facebook page and to use as a letter head in mailouts.
My ideal clients are those who want to create change in their lives and who invest money in themselves and their personal and spiritual growth.
I am different to regular life coaches as my sessions have a spiritual twist to them creating much deeper change in my clients.
I would like the banner to be mainly font with the title of the progam: 9 Paths Home Again (no other wording) (something along the lines of the Blackjack font) and that ties in with the theme of my website. I'm not sure what else I want with it and am looking for ideas.
Website:
www.quillorabalancecare.com.au
I also have a current facebook page for the business:
https://www.facebook.com/Quillora-Balance-Care-402715938846102/
(Note: I am about to drop my logo and business name and move to using my own name - the rest of the website will remain the same).
I have attached a doc with the draft of what wording will be on the website page any advertising will link to, to give you an idea of what the program is about.

Target Market(s)

People who invest money on themselves who are looking to improve their emotional well being and creating change in their life. Majority are middle aged women (also younger females and some men)

Industry/Entity Type

Health And Wellness

Font styles to use
Other font styles liked:
• I like Blackjack and Amienne. Along those lines.

Requirements
Must have
• Attractive, modern and GREAT font.
Nice to have
• Surprise me with something amazing!
• I love the colours in the 2 images I have up loaded as they represent the heart chakra colours. They could be a feature on the banner or blurred into the background.
Should not have
• Even though my work is quite spiritual I don't want it to look woo woo (meaning airy fairy spiritual stuff!)

```html
<!DOCTYPE html>
<html lang="en">
<head>
<meta charset="utf-8">
<title>9 Paths Home Again – Banner</title>
<link rel="stylesheet" href="https://fonts.googleapis.com/css2?family=Lobster+Two:wght@700&family=Oswald:wght@300;400&display=swap">
<style>
  :root {
    --page-bg: #f2eef0;
    --purple-deep: #8c13a8;
    --purple-mid: #a52cbf;
    --purple-light: #c05ad4;
    --white: #ffffff;
    --pill-shade: #dcdcdc;
    --ink: #2b2430;
    --leaf-light: #a6e07e;
    --leaf-green: #5c9c38;
    --leaf-bright: #8cc65c;
    --leaf-dark: #24513a;
    --lotus-pink: #f08ccb;
    --stone-grey: #6f706a;
    --herb-plum: #8a5a78;
    --ring-grey: #d9d4d6;
  }
  html, body {
    margin: 0;
    padding: 0;
    width: 1200px;
    height: 1200px;
    overflow: hidden;
    background: var(--page-bg);
  }
  .stage {
    position: relative;
    width: 1200px;
    height: 1200px;
  }
  .banner {
    position: absolute;
    left: 40px;
    top: 366px;
    width: 1245px;
    height: 520px;
    transform: scale(0.9);
    transform-origin: 0 0;
    overflow: hidden;
    background:
      radial-gradient(ellipse 420px 300px at 330px 180px, rgba(255,255,255,0.16), transparent 70%),
      linear-gradient(160deg, var(--purple-light) 0%, var(--purple-mid) 40%, var(--purple-deep) 100%);
    box-shadow: 0 10px 30px rgba(60, 20, 70, 0.25);
  }
  .title {
    position: absolute;
    left: 92px;
    top: 28px;
    margin: 0;
    z-index: 3;
    font-family: "Lobster Two", cursive;
    font-weight: 700;
    color: var(--white);
    line-height: 1;
    text-shadow: 0 4px 8px rgba(60, 0, 80, 0.45);
  }
  .title-line { display: block; }
  .title-line--top {
    font-size: 140px;
    padding-left: 14px;
  }
  .title-line--bottom {
    font-size: 104px;
    margin-top: -12px;
  }
  .tagline {
    position: absolute;
    left: 53px;
    top: 325px;
    width: 640px;
    height: 72px;
    margin: 0;
    z-index: 1;
    border-radius: 36px 0 0 36px;
    background: linear-gradient(180deg, var(--white) 0%, #f4f4f4 60%, var(--pill-shade) 100%);
    box-shadow: 0 3px 8px rgba(40, 0, 60, 0.35);
    box-sizing: border-box;
    padding-left: 33px;
    display: flex;
    align-items: center;
    font-family: "Oswald", sans-serif;
    font-weight: 400;
    font-size: 31px;
    letter-spacing: -0.3px;
    color: var(--ink);
  }
  .website {
    position: absolute;
    left: 92px;
    top: 428px;
    margin: 0;
    z-index: 3;
    font-family: "Oswald", sans-serif;
    font-weight: 300;
    font-size: 31px;
    color: var(--white);
    letter-spacing: 0.2px;
  }
  .visual {
    position: absolute;
    left: 0;
    top: 0;
    z-index: 2;
    width: 1245px;
    height: 520px;
  }
</style>
</head>
<body>
<div class="stage">
  <section class="banner">
    <svg class="visual" viewBox="0 0 1245 520" xmlns="http://www.w3.org/2000/svg">
      <defs>
        <linearGradient id="lotus-base" x1="0" y1="0" x2="0" y2="1">
          <stop offset="0" stop-color="var(--leaf-green)"/>
          <stop offset="0.5" stop-color="var(--leaf-bright)"/>
          <stop offset="1" stop-color="var(--leaf-dark)"/>
        </linearGradient>
        <radialGradient id="lotus-glow" cx="880" cy="370" r="190" gradientUnits="userSpaceOnUse">
          <stop offset="0" stop-color="var(--lotus-pink)" stop-opacity="0.85"/>
          <stop offset="0.55" stop-color="var(--lotus-pink)" stop-opacity="0.35"/>
          <stop offset="1" stop-color="var(--lotus-pink)" stop-opacity="0"/>
        </radialGradient>
        <radialGradient id="stone-tone" cx="0.5" cy="0.45" r="0.6">
          <stop offset="0" stop-color="#8d8e86"/>
          <stop offset="1" stop-color="var(--stone-grey)"/>
        </radialGradient>
        <linearGradient id="herb-tone" x1="0" y1="0" x2="0" y2="1">
          <stop offset="0" stop-color="#7b7680"/>
          <stop offset="0.55" stop-color="var(--herb-plum)"/>
          <stop offset="1" stop-color="#d9b9a6"/>
        </linearGradient>
      </defs>

      <!-- white swoosh band -->
      <path class="swoosh" d="M692 28 C730 24 760 14 778 0 L900 0 L900 520 L652 520 C612 455 616 380 646 308 C680 230 742 150 692 28 Z" fill="var(--white)"/>
      <!-- light green frame -->
      <path class="frame" d="M748 0 C900 4 1040 50 1112 132 C1176 215 1184 330 1154 425 C1135 475 1115 505 1095 520 L662 520 C628 460 630 385 660 315 C692 240 777 160 748 0 Z" fill="var(--leaf-light)"/>
      <!-- photo area -->
      <g role="img" aria-label="Photograph of a pink lotus flower on a lily pad against a soft green background">
        <path d="M764 8 C900 12 1030 60 1100 140 C1160 220 1170 330 1140 420 C1120 470 1100 500 1080 520 L676 520 C644 460 644 390 674 320 C704 250 790 170 764 8 Z" fill="url(#lotus-base)"/>
        <path d="M764 8 C900 12 1030 60 1100 140 C1160 220 1170 330 1140 420 C1120 470 1100 500 1080 520 L676 520 C644 460 644 390 674 320 C704 250 790 170 764 8 Z" fill="url(#lotus-glow)"/>
      </g>

      <!-- upper circle -->
      <circle cx="1088" cy="130" r="116" fill="var(--leaf-light)"/>
      <circle cx="1088" cy="130" r="108" fill="var(--ring-grey)"/>
      <circle cx="1088" cy="130" r="98" fill="url(#stone-tone)" role="img" aria-label="Photograph of a stone meditation statue"/>

      <!-- lower circle -->
      <circle cx="1140" cy="378" r="92" fill="var(--leaf-light)"/>
      <circle cx="1140" cy="378" r="85" fill="var(--ring-grey)"/>
      <circle cx="1140" cy="378" r="76" fill="url(#herb-tone)" role="img" aria-label="Photograph of a bowl of dried rose petals and herbs"/>
    </svg>

    <h1 class="title">
      <span class="title-line title-line--top">9 paths</span>
      <span class="title-line title-line--bottom">home again</span>
    </h1>
    <p class="tagline">Seeing the world from the eyes of your heart</p>
    <p class="website">www.quillorabalancecare.com.au</p>
  </section>
</div>
</body>
</html>
```